VeloRoot Sample Packaging Design

We need a design - with assistance on logo and colours - of a box containing sample sachets of a new natural sports supplement for endurance athletes.
We have an idea of logo and colours but would like input, ideas and assistance to create a cool new brand.

The product is based on natural beetroot powder which is scientifically backed to improve sports performance.
We like clean minimal branding that looks scientific - such as Kestrel Fuel, Stack Grains, Cortex Well Max and TuL Omni Drive sachets.

Attached is the type of package we will be using with matt black sachets, so clean white with potentially a beetroot colour (hex 691a40??) and grey (a3b2c2??) but we would like your professional and creative input.

I have attached a rough logo mock up of the logo I designed, happy for you to develop this by making it a bit cleaner (left edges angled or curved maybe- change font also maybe??) or your own ideas if clean, simple and effective. I based mine off the Far Meridian logo and PB works well with VeloRoot and Personal Best.

The final design should be clean, minimalist, high end sports supplement with a science and natural beetroot feel.
Box size: 300mm x 130mm x 14mm

Target Market(s)

Elite athletes and professionals wanting natural and science-backed supplements that work. Probably mainly men.
The customers are long distance sportspeople and NOT bodybuilders! Including triathletes, cyclists, long distance runners and swimmers.
The brand must also appeal to club level athletes and weekend warriors (but this should be easy if it's targeted at elite level first)

Industry/Entity Type

Supplement

Font styles to use
Sans Serif

Colors

Designer to choose colors to be used in the design.

Requirements
Must have
• - New logo (I like the Far Meridian logo but open to new ideas!)
• - Clean, scientific look with a twist of "I'm natural and not full of sports supplement junk!!"
• - A shade of beetroot red/purple as the signature colour, without looking too feminine.
• - Our slogan is "Beat your best"
Should not have
• A bodybuilder look.

```html
<!DOCTYPE html>
<html lang="en">
<head>
<meta charset="utf-8">
<title>VeloRoot Beetroot Raw Powder</title>
<link rel="stylesheet" href="https://fonts.googleapis.com/css2?family=Bebas+Neue&family=Arimo:wght@400&display=swap">
<style>
  :root {
    --frame-grey: #878889;
    --paper: #ffffff;
    --ink: #4a4a4c;
    --beet-deep: #c4084f;
    --beet-bright: #e8385a;
    --tick-plum: #a63a69;
    --rule: #6d6d6f;
    --leaf: #6a9a1e;
  }
  * { margin: 0; padding: 0; box-sizing: border-box; }
  html, body { width: 842px; height: 1200px; overflow: hidden; background: var(--frame-grey); }
  .canvas { position: relative; width: 842px; height: 1200px; background: var(--frame-grey); }
  .panel { position: absolute; left: 39px; top: 53px; width: 754px; height: 1098px; background: var(--paper); }

  .brand-name {
    position: absolute; left: 86px; top: 370px;
    font-family: "Bebas Neue", sans-serif; font-size: 190px; line-height: 1;
    color: var(--ink); letter-spacing: 2px;
  }
  .product-lines {
    position: absolute; left: 394px; top: 528px;
    font-family: "Bebas Neue", sans-serif; font-size: 68px; line-height: 61px;
    color: var(--ink); letter-spacing: 0.5px;
  }
  .product-lines .accent { color: var(--beet-bright); }

  .beet-illustration {
    position: absolute; left: 433px; top: 720px; width: 182px; height: 194px;
    background: radial-gradient(circle at 45% 55%, var(--beet-bright), var(--beet-deep) 70%);
    border-radius: 50% 50% 45% 45%;
  }

  .claims {
    position: absolute; left: 40px; top: 945px; width: 674px; height: 53px;
    border-top: 2px solid var(--rule); border-bottom: 2px solid var(--rule);
    display: flex; align-items: center; justify-content: center; gap: 14px;
    font-family: "Bebas Neue", sans-serif; font-size: 36px; color: var(--ink);
  }
  .claim { display: flex; align-items: center; gap: 6px; }
  .claim svg { width: 24px; height: 24px; }

  .usage {
    position: absolute; left: 218px; top: 1021px;
    display: flex; gap: 16px;
    font-family: "Arimo", sans-serif; font-size: 16px; line-height: 17px; color: var(--ink);
  }
  .usage-item { display: flex; align-items: center; gap: 4px; }
  .usage-item svg { width: 42px; height: 42px; }
</style>
</head>
<body>
<div class="canvas">
  <div class="panel">
    <div class="brand-name">VeloRoot</div>

    <div class="product-lines">
      NATURALLY<br>
      <span class="accent">BEETROOT</span><br>
      RAW POWDER
    </div>

    <div class="beet-illustration" role="img" aria-label="Illustration of a whole beetroot with green leaves beside a cut beetroot slice"></div>

    <div class="claims">
      <span class="claim">
        <svg viewBox="0 0 24 24" aria-hidden="true"><circle cx="12" cy="12" r="11" fill="var(--tick-plum)"/><path d="M6.5 12.5l3.5 3.5 7-8" fill="none" stroke="#fff" stroke-width="2.6" stroke-linecap="round" stroke-linejoin="round"/></svg>
        100% PURE
      </span>
      <span class="claim">
        <svg viewBox="0 0 24 24" aria-hidden="true"><circle cx="12" cy="12" r="11" fill="var(--tick-plum)"/><path d="M6.5 12.5l3.5 3.5 7-8" fill="none" stroke="#fff" stroke-width="2.6" stroke-linecap="round" stroke-linejoin="round"/></svg>
        GLUTEN FREE
      </span>
      <span class="claim">
        <svg viewBox="0 0 24 24" aria-hidden="true"><circle cx="12" cy="12" r="11" fill="var(--tick-plum)"/><path d="M6.5 12.5l3.5 3.5 7-8" fill="none" stroke="#fff" stroke-width="2.6" stroke-linecap="round" stroke-linejoin="round"/></svg>
        EXCELLENT TASTE
      </span>
    </div>

    <div class="usage">
      <div class="usage-item">
        <svg viewBox="0 0 42 42" aria-hidden="true"><circle cx="21" cy="21" r="20" fill="var(--beet-bright)"/><rect x="14" y="10" width="14" height="22" rx="1.5" fill="none" stroke="#fff" stroke-width="2"/></svg>
        <span>1 Serving<br>Per Sachet</span>
      </div>
      <div class="usage-item">
        <svg viewBox="0 0 42 42" aria-hidden="true"><circle cx="21" cy="21" r="20" fill="var(--beet-bright)"/><path d="M13 11h16l-2 21H15z" fill="none" stroke="#fff" stroke-width="2" stroke-linejoin="round"/><path d="M14.5 20h13" stroke="#fff" stroke-width="2"/></svg>
        <span>Just Add Water,<br>Shake &amp; Go!</span>
      </div>
    </div>
  </div>
</div>
</body>
</html>
```